Photo Storage Service - Web Application

This is web design for a simple photo storage service.
There is a web page and on the left side is a list of folders and on the right side there are photo thumbnails. By pressing a photo thumbnail, they will see the full size (it's just a link to a different page).
This project is limited only to ONE page, which is the page with the folders list and the thumbnails. However it contains some features that I will try to list here:
- Name of the service: Teso Vault
- Location of account: http://username.tesovault.example
- Folder list: Show all folders belonging to the user. Because you have to be able to drag photos to a folder, they have to be visible and cannot be hidden behind a menu item etc.
- Thumbnails with photos (in the future also videos)
- Adjusted view with smaller thumbnails and less space for folder list (so it is possible to view a larger quantity of thumbnails)- Select multiple thumbnails with rectangle- Show that a thumbnail is selected (maybe bold border?)
- Simple mobile view, but no emphasis on the mobile view in this design project.
- Drag one or more selected photos to a folder
- Delete one or more selected photos
- Drag a folder to another folder
- Rename folder
- Delete folder
- Create folder
- Show progress when deleting/moving (because it calls for every photo, so if there are 100 photos, it will delete 1 by 1 and it will take about 10 seconds - you could show progress bar or equivalent)
Background information: This is for a photo storage service NOT intended for sharing photos, but intended to indefinitely store photos and for yourself to browse your own photos.
It is a design requirement that it loads extremely fast. So we need to limit as much as possible extra graphics that cannot be done by CSS and other external libraries.
(I know this is ONLY design and nothing to do with CSS or libraries, but I can assess from the design if it might be heavy to load when implemented)
I have attached a crude screenshot of the current design, just for your understanding. It should not match this design and you are not in any way supposed to FIT your design into this same style or structure.
Target Market(s)
Consumers
Number of Pages Required
1 page

```html
<!DOCTYPE html>
<html lang="en">
<head>
<meta charset="utf-8">
<title>Teso Vault — Photo Storage</title>
<link href="https://fonts.googleapis.com/css2?family=Montserrat:wght@400;500;600;700&display=swap" rel="stylesheet">
<style>
:root{
  --page:#eceff2;
  --side-top:#44a7a9;
  --side-bottom:#1b9bdb;
  --side-foot:#1a8fcc;
  --accent:#2b9fc6;
  --ink:#2f3f47;
  --muted:#9aa6ad;
  --line:#e6eaed;
  --panel:#ffffff;
  --soft:#f6f8f9;
  --track:#dcecf3;
}
*{box-sizing:border-box;margin:0;padding:0}
html,body{width:1200px;height:2359px;overflow:hidden}
body{background:var(--page);font-family:"Montserrat",Arial,sans-serif;color:var(--ink);position:relative}

.brand-mark{position:absolute;left:0;right:0;top:62px;display:flex;align-items:center;justify-content:center;gap:14px}
.brand-mark .dot{width:74px;height:74px;border-radius:50%;background:var(--accent)}
.brand-mark .name{font-size:24px;font-weight:600;color:var(--accent);letter-spacing:.5px}

.screen{position:absolute;display:flex;background:var(--panel);overflow:hidden;box-shadow:0 10px 30px rgba(40,60,80,.08)}
.screen-overview{left:275px;top:226px;width:637px;height:387px}
.screen-select{left:285px;top:744px;width:630px;height:431px}
.screen-progress{left:285px;top:1235px;width:630px;height:431px}
.screen-viewer{left:288px;top:1727px;width:627px;height:431px}

.sidebar{width:148px;flex:none;position:relative;background:linear-gradient(180deg,var(--side-top),var(--side-bottom));color:#fff}
.sidebar-brand{display:flex;align-items:center;gap:7px;height:42px;padding-left:12px;font-size:12px;font-weight:700;letter-spacing:.3px}
.sidebar-brand i{width:15px;height:15px;border-radius:50%;background:#fff;opacity:.9}
.folders{list-style:none;padding:8px 0 0 13px;position:relative}
.folders::after{content:"";position:absolute;right:6px;top:6px;width:2px;height:110px;background:rgba(255,255,255,.45);border-radius:2px}
.folder{display:flex;align-items:center;gap:8px;height:20.2px;font-size:5.6px;font-weight:500;text-transform:uppercase;letter-spacing:.3px;opacity:.85}
.folder i{width:10px;height:10px;border-radius:50%;background:rgba(255,255,255,.28);flex:none}
.folder.inbox{font-size:7px;text-transform:none;font-weight:700;opacity:1}
.folder.active{opacity:1;font-weight:700}
.folder.active i{width:13px;height:13px;background:#fff}
.folder.sub{height:14px;padding-left:24px;text-transform:none;font-weight:700;font-size:5.6px}
.sidebar-foot{position:absolute;left:0;right:0;bottom:0;height:20px;background:var(--side-foot);display:flex;align-items:center;gap:7px;padding-left:10px;font-size:5px}
.sidebar-foot i{width:12px;height:6px;border-radius:3px;border:1px solid #fff}

.main{flex:1;position:relative;background:var(--panel)}
.topbar{height:41px;display:flex;align-items:center;justify-content:space-between;padding:0 18px 0 19px;border-bottom:1px solid var(--line)}
.welcome{font-size:6px;color:var(--muted)}
.welcome b{color:var(--accent);font-weight:600}
.topbar-right{display:flex;align-items:center;gap:10px}
.btn-create{height:13px;padding:0 12px;border:1px solid var(--accent);border-radius:7px;font-size:5px;color:var(--accent);display:flex;align-items:center;text-transform:uppercase;letter-spacing:.3px}
.avatar{width:16px;height:16px;border-radius:50%;background:linear-gradient(135deg,#c99b83,#7d5443)}

.album-head{display:flex;align-items:center;justify-content:space-between;padding:14px 18px 10px 19px}
.album-title{display:flex;align-items:center;gap:5px;font-size:11px;font-weight:600;color:var(--accent)}
.album-title i{width:6px;height:6px;border:1px solid var(--accent);border-radius:50%}
.tools{display:flex;gap:5px}
.tools i{width:13px;height:13px;border-radius:50%;background:#d7e6ec}
.tools i.on{background:var(--accent)}

.grid{display:grid;grid-template-columns:repeat(4,100px);gap:12px;padding:0 0 0 19px}
.thumb{height:100px;position:relative}
.thumb .pick{position:absolute;left:5px;top:5px;width:7px;height:7px;border-radius:50%;border:1px solid #fff}
.t1{background:linear-gradient(160deg,#8a8f7a,#46524a)}
.t2{background:linear-gradient(160deg,#c4a06a,#6b5337)}
.t3{background:linear-gradient(160deg,#7f9468,#4c5a42)}
.t4{background:linear-gradient(160deg,#b9c0c2,#5d6664)}
.t5{background:linear-gradient(160deg,#6f6c63,#2f302c)}
.t6{background:linear-gradient(160deg,#7a6a55,#3f3a33)}
.t7{background:linear-gradient(160deg,#5f7a4d,#34412d)}
.t8{background:linear-gradient(160deg,#c9cccb,#6d7572)}
.t9{background:linear-gradient(160deg,#7d9c6d,#4f5e47)}
.t10{background:linear-gradient(160deg,#8b7a5a,#4a4536)}
.t11{background:linear-gradient(160deg,#a7a9a0,#59574d)}
.t12{background:linear-gradient(160deg,#9aa8a6,#4c5653)}
.scroll{position:absolute;right:8px;top:56px;width:2px;height:150px;background:var(--accent);border-radius:2px}

.veil{position:absolute;inset:0;background:rgba(255,255,255,.72)}
.modal{position:absolute;left:71px;top:153px;width:338px;height:129px;background:#fff;box-shadow:0 8px 28px rgba(30,50,70,.16);padding:0 33px}
.spinner{display:block;margin:20px auto 0}
.bar{margin-top:13px;height:8px;border-radius:4px;background:var(--track);overflow:hidden}
.bar span{display:block;width:48%;height:100%;background:var(--accent);border-radius:4px}
.bar-labels{display:flex;justify-content:space-between;margin-top:10px;font-size:5.5px;color:var(--ink)}
.bar-labels b{color:var(--accent)}

.viewer-head{display:flex;align-items:center;justify-content:space-between;padding:14px 14px 0 20px}
.viewer-title{font-size:10px;font-weight:600;color:var(--accent)}
.close{width:16px;height:16px;border-radius:50%;background:var(--accent);display:flex;align-items:center;justify-content:center}
.photo{position:absolute;left:20px;top:71px;width:439px;height:291px;background:linear-gradient(120deg,#2f2a25 0%,#5a5046 45%,#8d8a84 70%,#3b362f 100%)}
.nav{position:absolute;top:50%;transform:translateY(-50%)}
.nav.prev{left:10px}
.nav.next{right:10px}

.site{position:absolute;left:0;right:0;top:2248px;text-align:center;font-size:16px;font-weight:500;color:var(--ink);letter-spacing:.3px}
</style>
</head>
<body>

<div class="brand-mark"><span class="dot"></span><span class="name">Teso Vault</span></div>

<!-- Overview -->
<section class="screen screen-overview">
  <aside class="sidebar">
    <div class="sidebar-brand"><i></i>Teso Vault</div>
    <ul class="folders">
      <li class="folder inbox"><i></i>Photo / Video Inbox</li>
      <li class="folder"><i></i>Timeline photos</li>
      <li class="folder"><i></i>80's party</li>
      <li class="folder active"><i></i>A day in Oslo</li>
      <li class="folder sub">Waterfalls</li>
      <li class="folder"><i></i>A tour of Svendborg</li>
      <li class="folder"><i></i>Alicante 2017</li>
      <li class="folder"><i></i>Bangkok</li>
      <li class="folder"><i></i>Birds lightly gathered ...</li>
      <li class="folder"><i></i>Waterfalls</li>
      <li class="folder"><i></i>Brazil</li>
      <li class="folder"><i></i>Days in Denmark</li>
      <li class="folder"><i></i>Christmas and new years</li>
      <li class="folder"><i></i>Mobile uploads</li>
      <li class="folder"><i></i>Sundarban</li>
      <li class="folder"><i></i>Tea garden</li>
    </ul>
  </aside>
  <div class="main">
    <header class="topbar"><p class="welcome">Welcome to <b>Lena Marsh</b></p><div class="topbar-right"><span class="btn-create">Create album</span><span class="avatar" role="img" aria-label="User profile photo"></span></div></header>
    <div class="album-head"><h2 class="album-title"><i></i>Waterfalls</h2><div class="tools"><i class="on"></i><i></i><i></i></div></div>
    <div class="grid">
      <div class="thumb t1" role="img" aria-label="Couple sitting by a waterfall"></div>
      <div class="thumb t2" role="img" aria-label="Waterfall in autumn forest"></div>
      <div class="thumb t3" role="img" aria-label="Person swimming in a pool"></div>
      <div class="thumb t4" role="img" aria-label="Misty waterfall in a gorge"></div>
      <div class="thumb t5" role="img" aria-label="Dark rocks and water"></div>
      <div class="thumb t6" role="img" aria-label="Couple by a waterfall"></div>
      <div class="thumb t7" role="img" aria-label="Cascade in green forest"></div>
      <div class="thumb t8" role="img" aria-label="Wide waterfall in mist"></div>
      <div class="thumb t9" role="img" aria-label="People walking in a stream"></div>
      <div class="thumb t10" role="img" aria-label="Small forest waterfall"></div>
      <div class="thumb t11" role="img" aria-label="Couple near falling water"></div>
      <div class="thumb t12" role="img" aria-label="Waterfall over rocks"></div>
    </div>
    <span class="scroll"></span>
  </div>
</section>

<!-- Selection -->
<section class="screen screen-select">
  <aside class="sidebar">
    <div class="sidebar-brand"><i></i>Teso Vault</div>
    <ul class="folders">
      <li class="folder inbox"><i></i>Photo / Video Inbox</li>
      <li class="folder"><i></i>Timeline photos</li>
      <li class="folder"><i></i>80's party</li>
      <li class="folder active"><i></i>A day in Oslo</li>
      <li class="folder sub">Waterfalls</li>
      <li class="folder"><i></i>A tour of Svendborg</li>
      <li class="folder"><i></i>Alicante 2017</li>
      <li class="folder"><i></i>Bangkok</li>
      <li class="folder"><i></i>Birds lightly gathered ...</li>
      <li class="folder"><i></i>Waterfalls</li>
      <li class="folder"><i></i>Brazil</li>
      <li class="folder"><i></i>Days in Denmark</li>
      <li class="folder"><i></i>Christmas and new years</li>
      <li class="folder"><i></i>Mobile uploads</li>
      <li class="folder"><i></i>Sundarban</li>
      <li class="folder"><i></i>Tea garden</li>
    </ul>
    <footer class="sidebar-foot"><i></i>© 2018 Teso Vault</footer>
  </aside>
  <div class="main">
    <header class="topbar"><p class="welcome">Welcome to <b>Lena Marsh</b></p><div class="topbar-right"><span class="btn-create">Create album</span><span class="avatar" role="img" aria-label="User profile photo"></span></div></header>
    <div class="album-head"><h2 class="album-title"><i></i>Waterfalls</h2><div class="tools"><i></i><i></i><i class="on"></i></div></div>
    <div class="grid">
      <div class="thumb t1" role="img" aria-label="Couple sitting by a waterfall"><span class="pick"></span></div>
      <div class="thumb t2" role="img" aria-label="Waterfall in autumn forest"><span class="pick"></span></div>
      <div class="thumb t3" role="img" aria-label="Person swimming in a pool"><span class="pick"></span></div>
      <div class="thumb t4" role="img" aria-label="Misty waterfall in a gorge"><span class="pick"></span></div>
      <div class="thumb t5" role="img" aria-label="Dark rocks and water"><span class="pick"></span></div>
      <div class="thumb t6" role="img" aria-label="Couple by a waterfall"><span class="pick"></span></div>
      <div class="thumb t7" role="img" aria-label="Cascade in green forest"><span class="pick"></span></div>
      <div class="thumb t8" role="img" aria-label="Wide waterfall in mist"><span class="pick"></span></div>
      <div class="thumb t9" role="img" aria-label="People walking in a stream"><span class="pick"></span></div>
      <div class="thumb t10" role="img" aria-label="Small forest waterfall"><span class="pick"></span></div>
      <div class="thumb t11" role="img" aria-label="Couple near falling water"><span class="pick"></span></div>
      <div class="thumb t12" role="img" aria-label="Waterfall over rocks"><span class="pick"></span></div>
    </div>
    <span class="scroll"></span>
  </div>
</section>

<!-- Progress -->
<section class="screen screen-progress">
  <aside class="sidebar">
    <div class="sidebar-brand"><i></i>Teso Vault</div>
    <ul class="folders">
      <li class="folder inbox"><i></i>Photo / Video Inbox</li>
      <li class="folder"><i></i>Timeline photos</li>
      <li class="folder"><i></i>80's party</li>
      <li class="folder active"><i></i>A day in Oslo</li>
      <li class="folder sub">Waterfalls</li>
      <li class="folder"><i></i>A tour of Svendborg</li>
      <li class="folder"><i></i>Alicante 2017</li>
      <li class="folder"><i></i>Bangkok</li>
      <li class="folder"><i></i>Birds lightly gathered ...</li>
      <li class="folder"><i></i>Waterfalls</li>
      <li class="folder"><i></i>Brazil</li>
      <li class="folder"><i></i>Days in Denmark</li>
      <li class="folder"><i></i>Christmas and new years</li>
      <li class="folder"><i></i>Mobile uploads</li>
      <li class="folder"><i></i>Sundarban</li>
      <li class="folder"><i></i>Tea garden</li>
    </ul>
    <footer class="sidebar-foot"><i></i>© 2018 Teso Vault</footer>
  </aside>
  <div class="main">
    <header class="topbar"><p class="welcome">Welcome to <b>Lena Marsh</b></p><div class="topbar-right"><span class="btn-create">Create album</span><span class="avatar" role="img" aria-label="User profile photo"></span></div></header>
    <div class="album-head"><h2 class="album-title"><i></i>Waterfalls</h2><div class="tools"><i></i><i></i><i class="on"></i></div></div>
    <div class="grid">
      <div class="thumb t1" role="img" aria-label="Couple sitting by a waterfall"><span class="pick"></span></div>
      <div class="thumb t2" role="img" aria-label="Waterfall in autumn forest"><span class="pick"></span></div>
      <div class="thumb t3" role="img" aria-label="Person swimming in a pool"><span class="pick"></span></div>
      <div class="thumb t4" role="img" aria-label="Misty waterfall in a gorge"><span class="pick"></span></div>
      <div class="thumb t5" role="img" aria-label="Dark rocks and water"><span class="pick"></span></div>
      <div class="thumb t6" role="img" aria-label="Couple by a waterfall"><span class="pick"></span></div>
      <div class="thumb t7" role="img" aria-label="Cascade in green forest"><span class="pick"></span></div>
      <div class="thumb t8" role="img" aria-label="Wide waterfall in mist"><span class="pick"></span></div>
      <div class="thumb t9" role="img" aria-label="People walking in a stream"></div>
      <div class="thumb t10" role="img" aria-label="Small forest waterfall"></div>
      <div class="thumb t11" role="img" aria-label="Couple near falling water"></div>
      <div class="thumb t12" role="img" aria-label="Waterfall over rocks"></div>
    </div>
    <span class="scroll"></span>
    <div class="veil"></div>
    <div class="modal">
      <svg class="spinner" width="22" height="22" viewBox="0 0 22 22"><path d="M11 2 A9 9 0 0 1 17 18" fill="none" stroke="var(--accent)" stroke-width="2" stroke-linecap="round"/></svg>
      <div class="bar"><span></span></div>
      <div class="bar-labels"><span>Uploading</span><b>48%</b></div>
    </div>
  </div>
</section>

<!-- Viewer -->
<section class="screen screen-viewer">
  <aside class="sidebar">
    <div class="sidebar-brand"><i></i>Teso Vault</div>
    <ul class="folders">
      <li class="folder inbox"><i></i>Photo / Video Inbox</li>
      <li class="folder"><i></i>Timeline photos</li>
      <li class="folder"><i></i>80's party</li>
      <li class="folder active"><i></i>A day in Oslo</li>
      <li class="folder sub">Waterfalls</li>
      <li class="folder"><i></i>A tour of Svendborg</li>
      <li class="folder"><i></i>Alicante 2017</li>
      <li class="folder"><i></i>Bangkok</li>
      <li class="folder"><i></i>Birds lightly gathered ...</li>
      <li class="folder"><i></i>Waterfalls</li>
      <li class="folder"><i></i>Brazil</li>
      <li class="folder"><i></i>Days in Denmark</li>
      <li class="folder"><i></i>Christmas and new years</li>
      <li class="folder"><i></i>Mobile uploads</li>
      <li class="folder"><i></i>Sundarban</li>
      <li class="folder"><i></i>Tea garden</li>
    </ul>
    <footer class="sidebar-foot"><i></i>© 2018 Teso Vault</footer>
  </aside>
  <div class="main">
    <div class="viewer-head">
      <h2 class="viewer-title">Waterfalls</h2>
      <span class="close"><svg width="8" height="8" viewBox="0 0 8 8"><path d="M1 1L7 7M7 1L1 7" stroke="#fff" stroke-width="1.3" stroke-linecap="round"/></svg></span>
    </div>
    <div class="photo" role="img" aria-label="Full-size photo of a couple embracing in front of a waterfall">
      <svg class="nav prev" width="8" height="12" viewBox="0 0 8 12"><path d="M6 1L1.5 6L6 11" fill="none" stroke="#fff" stroke-width="1.6" stroke-linecap="round"/></svg>
      <svg class="nav next" width="8" height="12" viewBox="0 0 8 12"><path d="M2 1L6.5 6L2 11" fill="none" stroke="#fff" stroke-width="1.6" stroke-linecap="round"/></svg>
    </div>
  </div>
</section>

<p class="site">www.tesovault.example</p>

</body>
</html>
```